Tavelin: A Friday night of the Kindled Word Flyer

We are holding 2 Friday night events, one on 10/25/19 and the other on 11/29/19.
The time frame is 6:30pm-9:00pm. These services will be a time of prayer/healing for the sick and will be prophetic as well. (There will be prophets prophesying over people)

The event is called: Tavelin: A Friday night of the Kindled Word
The flyer should also include the phrase/excerpt: "And they prophesied also".

Keywords/Phrases: Prophetic, Healing, Climbing in the Spirit, Higher level of Anointing...

Target Market(s)

those looking for healing, seeking a word from God

Colors

Designer to choose colors to be used in the design.

Requirements
Must have
• The event is called: Tavelin: A Friday night of the Kindled Word
• The flyer should also include the phrase/excerpt: "And they prophesied also".
• It must include the Quorvel logo attached, either is fine, we have attached two different versions.
• It must have the dates, location, time
• Dates: October 25, 2019 and November 29, 2019
• Location: Loftmere Community Center
• (Downtown Portland) 248 Wendlow Street
• Portland, ME 04102
• Time: 6:30pm-9:00pm
• Contact Info: Tel. 207-583-2914
• email: contact@ambervale.example
• web: www.quorvel.example
Nice to have
• creativity in color scheme, the meaning of the word Tavelin conveyed in a classy artistic way/design.
Should not have
• Crosses, pictures of churches

```html
<!DOCTYPE html>
<html lang="en">
<head>
<meta charset="utf-8">
<title>Tavelin: A Friday night of the Kindled Word</title>
<link rel="stylesheet" href="https://fonts.googleapis.com/css2?family=Cinzel:wght@400;700&family=Oswald:wght@400&family=Open+Sans:wght@400;600&display=swap">
<style>
  :root {
    --page: #4a4a4a;
    --sky-top: #8fa3b8;
    --sky-mid: #3f6a96;
    --navy: #0f2e5a;
    --navy-deep: #0a2247;
    --orange: #f7941d;
    --white: #ffffff;
    --rule: #d9e1ea;
  }
  * { margin: 0; padding: 0; box-sizing: border-box; }
  html, body { width: 1200px; height: 800px; overflow: hidden; background: var(--page); }
  .flyer {
    position: absolute; left: 330px; top: 18px;
    width: 540px; height: 764px; overflow: hidden;
    color: var(--white);
  }
  .flyer__photo {
    position: absolute; inset: 0;
    background:
      radial-gradient(ellipse 140px 300px at 110px 330px, rgba(30,45,70,.55), transparent 70%),
      linear-gradient(180deg, var(--sky-top) 0%, #7e9ab6 22%, var(--sky-mid) 48%, var(--navy) 72%, var(--navy-deep) 100%);
  }
  .flyer__emblem {
    position: absolute; left: 285px; top: 40px; width: 110px; height: 130px;
    border-radius: 50%;
    background: radial-gradient(circle, rgba(247,148,29,.55), rgba(247,148,29,0) 70%);
  }
  .event {
    position: absolute; left: 170px; width: 350px; top: 170px;
    text-align: center;
  }
  .event__title {
    font-family: "Cinzel", serif; font-weight: 400;
    font-size: 74px; line-height: 1; color: var(--orange); letter-spacing: 1px;
  }
  .event__subtitle {
    font-family: "Oswald", sans-serif; font-weight: 400;
    font-size: 31px; line-height: 1.15; margin-top: 8px; letter-spacing: .5px;
  }
  .event__verse, .event__dates, .event__time, .event__venue {
    font-family: "Cinzel", serif; font-weight: 700;
  }
  .event__verse { font-size: 15px; letter-spacing: 2px; margin-top: 8px; }
  .event__dates { font-size: 19px; letter-spacing: 2.5px; line-height: 1.25; margin-top: 10px; }
  .event__time { font-size: 18px; letter-spacing: 3px; margin-top: 10px; }
  .event__venue { font-size: 11.5px; letter-spacing: 2px; line-height: 1.9; margin-top: 12px; }
  .call {
    position: absolute; left: 300px; top: 595px;
    display: flex; align-items: center; gap: 12px;
    font-family: "Open Sans", sans-serif;
  }
  .call__label { font-size: 17px; font-weight: 600; letter-spacing: .5px; }
  .call__number { font-size: 20px; }
  .footer__rule {
    position: absolute; left: 0; right: 0; top: 652px; height: 2px; background: var(--rule);
  }
  .brand {
    position: absolute; left: 30px; top: 672px;
    display: flex; align-items: center; gap: 8px;
    font-family: "Cinzel", serif; font-weight: 400; font-size: 30px; color: var(--white);
  }
  .brand__dot { width: 12px; height: 12px; border-radius: 50%; background: var(--orange); }
  .contact {
    position: absolute; display: flex; align-items: center; gap: 10px;
    font-family: "Open Sans", sans-serif; font-size: 15px;
  }
  .contact--web { left: 315px; top: 688px; }
  .contact--mail { left: 30px; top: 726px; }
</style>
</head>
<body>
<main class="flyer">
  <div class="flyer__photo" role="img" aria-label="Photo of a young man praying with clasped hands against a blue cloudy sky"></div>
  <div class="flyer__emblem" role="img" aria-label="Orange flame emblem"></div>

  <section class="event">
    <h1 class="event__title">TAVELIN</h1>
    <p class="event__subtitle">A FRIDAY NIGHT<br>OF THE KINDLED WORD</p>
    <p class="event__verse">AND THEY PROPHESIED ALSO</p>
    <p class="event__dates">OCTOBER 25, 2019<br>&amp;<br>NOVEMBER 29, 2019</p>
    <p class="event__time">6:30PM-9:00PM</p>
    <p class="event__venue">LOFTMERE COMMUNITY CENTER<br>(DOWNTOWN PORTLAND) 248 WENDLOW STREET<br>PORTLAND, ME 04102</p>
  </section>

  <div class="call">
    <svg width="40" height="40" viewBox="0 0 40 40" aria-hidden="true">
      <path d="M9 6l6 7-3 4c2 4 5 7 9 9l4-3 7 6-4 5C17 34 6 23 4 10z" fill="var(--orange)"/>
      <path d="M24 6a10 10 0 0 1 10 10M24 11a5 5 0 0 1 5 5" stroke="var(--orange)" stroke-width="2.5" fill="none" stroke-linecap="round"/>
    </svg>
    <div>
      <div class="call__label">CALL US</div>
      <div class="call__number">207-583-2914</div>
    </div>
  </div>

  <div class="footer__rule"></div>

  <div class="brand"><span class="brand__dot"></span>QUORVEL</div>

  <div class="contact contact--web">
    <svg width="22" height="22" viewBox="0 0 22 22" aria-hidden="true">
      <g stroke="var(--orange)" stroke-width="1.6" fill="none">
        <circle cx="11" cy="11" r="9"/><ellipse cx="11" cy="11" rx="4" ry="9"/>
        <path d="M2 11h18M4 6h14M4 16h14"/>
      </g>
    </svg>
    <span>www.quorvel.example</span>
  </div>

  <div class="contact contact--mail">
    <svg width="28" height="20" viewBox="0 0 28 20" aria-hidden="true">
      <rect x="1" y="1" width="26" height="18" fill="var(--orange)"/>
      <path d="M1 1l13 10L27 1" stroke="var(--navy-deep)" stroke-width="1.6" fill="none"/>
    </svg>
    <span>contact@ambervale.example</span>
  </div>
</main>
</body>
</html>
```